Business Card Design

We are looking for a double sided business card.

On one side would be our logo

On the Other Side

Martin Kolby
Sales and Marketing

Phone/Text Logo and 530-418-2763
Email Logo and info@plumvalepets.com
Website Logo and www.plumvalepets.com
Facebook Logo and plumvale pets
Instagram Logo and plumvale_pets

Target Market(s)

Pet owners

Contact Information for Business Card

In project description

Requirements
Must have
• Logo

```html
<!DOCTYPE html>
<html lang="en">
<head>
<meta charset="utf-8">
<title>Plumvale Pets – Business Card</title>
<link href="https://fonts.googleapis.com/css2?family=Montserrat:wght@500;800&family=Barlow:wght@400&display=swap" rel="stylesheet">
<style>
  :root {
    --canvas: #eeeeee;
    --ink: #000000;
    --white: #ffffff;
    --orange: #f39200;
    --orange-deep: #e07f1d;
    --orange-band: #e8861f;
    --yellow: #f5b91c;
    --silver: #d9d9d9;
  }
  * { margin: 0; padding: 0; box-sizing: border-box; }
  html, body { width: 1200px; height: 1200px; overflow: hidden; }
  body { background: var(--canvas); position: relative; font-family: "Barlow", sans-serif; }

  .card { position: absolute; left: 217px; width: 768px; height: 437px; overflow: hidden; }
  .card--front { top: 113px; }
  .card--back { top: 649px; }
  .card__art { position: absolute; inset: 0; width: 100%; height: 100%; display: block; }

  .brand { position: absolute; display: flex; flex-direction: column; align-items: center; gap: 10px; }
  .brand__row { display: flex; align-items: center; gap: 12px; }
  .brand__dot { width: 34px; height: 34px; border-radius: 50%; background: var(--orange); }
  .brand__name { font-family: "Montserrat", sans-serif; font-weight: 800; font-size: 30px; color: var(--silver); letter-spacing: 0.5px; white-space: nowrap; }
  .brand__url { font-family: "Montserrat", sans-serif; font-weight: 500; font-size: 10px; letter-spacing: 3px; color: var(--orange); }
  .card--front .brand { left: 236px; top: 143px; transform: translateX(-50%); }
  .card--back .brand { left: 491px; top: 218px; transform: translateX(-50%) scale(1.1); }

  .person { position: absolute; left: 443px; top: 92px; }
  .person__name { font-family: "Montserrat", sans-serif; font-weight: 800; font-size: 22px; color: var(--white); text-transform: uppercase; }
  .person__name span { color: var(--orange); }
  .person__role { font-family: "Montserrat", sans-serif; font-weight: 500; font-size: 11.5px; color: var(--white); margin-top: 1px; }

  .contacts { position: absolute; left: 441px; top: 185px; list-style: none; }
  .contacts__item { display: flex; align-items: center; height: 21px; margin-bottom: 12.5px; color: var(--white); font-size: 19px; }
  .contacts__icon { width: 21px; height: 21px; border-radius: 3px; background: var(--orange); margin-right: 12px; flex: none; display: flex; align-items: center; justify-content: center; }
  .contacts__icon svg { width: 13px; height: 13px; }
</style>
</head>
<body>

<section class="card card--front">
  <svg class="card__art" viewBox="0 0 1151 655" preserveAspectRatio="none" aria-hidden="true">
    <defs>
      <linearGradient id="warm" x1="0" y1="0" x2="0.3" y2="1">
        <stop offset="0" stop-color="#e8861f"/><stop offset="1" stop-color="#f5b91c"/>
      </linearGradient>
      <linearGradient id="band" x1="0" y1="0" x2="0.3" y2="1">
        <stop offset="0" stop-color="#c9691f"/><stop offset="1" stop-color="#f0901c"/>
      </linearGradient>
    </defs>
    <rect width="1151" height="655" fill="#ef8d1c"/>
    <path d="M0 0 H120 V655 H0 Z M0 0 C0 0 40 0 40 0 C30 260 240 420 252 655 H0 Z" fill="url(#warm)"/>
    <path d="M40 150 C40 330 200 440 330 520 C410 570 460 610 478 655 H252 C250 560 200 520 150 450 C80 350 40 300 40 150 Z" fill="url(#band)"/>
    <path d="M100 0 H920 C1050 0 1140 100 1151 230 V655 H478 C420 530 280 470 170 390 C60 310 30 220 42 160 C50 90 70 40 100 0 Z" fill="#000"/>
  </svg>

  <div class="brand">
    <div class="brand__row"><span class="brand__dot"></span><span class="brand__name">PLUMVALE PETS</span></div>
    <span class="brand__url">WWW.PLUMVALEPETS.COM</span>
  </div>

  <div class="person">
    <h1 class="person__name">Martin <span>Kolby</span></h1>
    <p class="person__role">Sales And Marketing</p>
  </div>

  <ul class="contacts">
    <li class="contacts__item"><span class="contacts__icon"><svg viewBox="0 0 24 24"><path d="M6.6 10.8a15 15 0 006.6 6.6l2.2-2.2a1 1 0 011-.25 11.4 11.4 0 003.6.57 1 1 0 011 1V20a1 1 0 01-1 1A17 17 0 013 4a1 1 0 011-1h3.5a1 1 0 011 1c0 1.25.2 2.45.57 3.6a1 1 0 01-.25 1z" fill="#000"/></svg></span>530-418-2763</li>
    <li class="contacts__item"><span class="contacts__icon"><svg viewBox="0 0 24 24"><rect x="3" y="6" width="18" height="12" fill="none" stroke="#000" stroke-width="2"/><path d="M3 6l9 7 9-7" fill="none" stroke="#000" stroke-width="2"/></svg></span>info@plumvalepets.com</li>
    <li class="contacts__item"><span class="contacts__icon"><svg viewBox="0 0 24 24" fill="none" stroke="#000" stroke-width="1.6"><circle cx="12" cy="12" r="9"/><ellipse cx="12" cy="12" rx="4" ry="9"/><path d="M3 12h18M5 7h14M5 17h14"/></svg></span>www.plumvalepets.com</li>
    <li class="contacts__item"><span class="contacts__icon"></span>plumvale_pets</li>
    <li class="contacts__item"><span class="contacts__icon"></span>plumvale pets</li>
  </ul>
</section>

<section class="card card--back">
  <svg class="card__art" viewBox="0 0 1151 655" preserveAspectRatio="none" aria-hidden="true">
    <rect width="1151" height="655" fill="#ef8d1c"/>
    <path d="M0 0 H40 C30 260 240 420 252 655 H0 Z" fill="url(#warm)"/>
    <path d="M40 150 C40 330 200 440 330 520 C410 570 460 610 478 655 H252 C250 560 200 520 150 450 C80 350 40 300 40 150 Z" fill="url(#band)"/>
    <path d="M100 0 H920 C1050 0 1140 100 1151 230 V655 H478 C420 530 280 470 170 390 C60 310 30 220 42 160 C50 90 70 40 100 0 Z" fill="#000"/>
  </svg>

  <div class="brand">
    <div class="brand__row"><span class="brand__dot"></span><span class="brand__name">PLUMVALE PETS</span></div>
    <span class="brand__url">WWW.PLUMVALEPETS.COM</span>
  </div>
</section>

</body>
</html>
```